Private Lending Company looking to have 3 Word Documents re-formatted, cleaned up and generally made

We have three word documents that we use for presentations.
a) The first document (Wholesale and Portfolio Investor Pack May 2016) has graphs incorporated which are currently blurred and perhaps not the most current data. All graphs have the source noted so these would need to be replaced with current data if it is available and generally cleaned up. The cover page requires our new logo (attached). The illustration on page 29 needs to be changed to a matrix or cube or something that represents/brings all the elements of page 29 (ie 4 bullet points) together. The whole document needs to look more corporate and professional.
b) The second and third documents (Talvora KRB Lending Guides July 2016 and Talvora Select Lending Guides July 2016) both require tidying up. Tables are not quite aligned, data within the tables is not lined up or consistent. Again, both documents need to be polished and given to look more corporate. Ensure the logo in the letterhead is the same size on each page.
Throughout all documents it is important to keep tables, shading, size etc consistent. Any table fill should be in the same blue (as per advert) throughout Documents 2 & 3.
We would like our corporate colours to be used not only in the letterhead but also in the font, the fill in the tables etc.
We have attached our logo, and a digital copy of an advert we recently used. The advert is attached more for your information - you do not need to use it at all.
The colours used in the advert are as follows:
Blue - RGB: R=30, G=30, B=59
Gold - RGB: R=227, G=205, B=152 (for table outlines)
Blue - CMYK: C=97%, M=87%, Y=45%, K=55%
Gold - CMYK: C=12%, M=21%, Y=51%, K=2% (for table outlines)
The blue in our logo is on the standard Word Pallette (Dark Blue, Text 2, Darker 25%)
The light blue featured in the tables of Document 1 can be: Blue, Accent 1, Lighter 80%. This also needs to be used consistently thoughout this document.
We would like all text to be in the same colour as the logo, although of course not necessarily the same font. Our preferred Font is Century Gothic.
Please direct any questions back to us.
It Company
- Calibri

```html
<!DOCTYPE html>
<html lang="en">
<head>
<meta charset="utf-8">
<title>Lending Process Matrix and Unemployment Rate</title>
<link rel="stylesheet" href="https://fonts.googleapis.com/css2?family=Didact+Gothic&family=Poppins:ital,wght@0,600;1,600&display=swap">
<style>
  :root {
    --page: #ffffff;
    --navy: #1e1e3b;
    --logo-blue: #17365d;
    --tile-top: #2a4674;
    --tile-bottom: #1e1e3b;
    --gold: #e3cd98;
    --gold-soft: #efe4c8;
    --tile-text: #ffffff;
    --grid: #d9ccaa;
    --text: #17365d;
  }
  * { margin: 0; padding: 0; box-sizing: border-box; }
  html, body { width: 944px; height: 1200px; overflow: hidden; background: var(--page); }
  .page { position: relative; width: 944px; height: 1200px; background: var(--page); }

  .matrix-arrows { position: absolute; left: 0; top: 0; width: 944px; height: 620px; }
  .matrix-tile {
    position: absolute;
    width: 211px; height: 206px;
    border-radius: 27px;
    background: linear-gradient(to bottom, var(--tile-top), var(--tile-bottom));
    border: 2px solid var(--gold);
    box-shadow: 0 2px 4px rgba(30,30,59,0.25);
    display: flex; align-items: center; justify-content: center;
    text-align: center;
    color: var(--tile-text);
    font-family: "Century Gothic", "Poppins", sans-serif;
    font-style: italic; font-weight: 600;
    font-size: 21px; line-height: 1.2;
    padding: 0 12px;
  }
  .tile-origination { left: 239px; top: 112px; align-items: flex-start; padding-top: 74px; }
  .tile-documentation { left: 469px; top: 112px; align-items: flex-start; padding-top: 62px; }
  .tile-asset { left: 240px; top: 344px; }
  .tile-portfolio { left: 469px; top: 342px; }

  .chart-frame {
    position: absolute; left: 143px; top: 631px;
    width: 638px; height: 372px;
    border: 1px solid var(--gold);
    background: var(--page);
  }
  .chart-frame svg { display: block; }
  .chart-title { font-family: "Century Gothic", "Poppins", sans-serif; font-weight: 600; font-size: 21px; fill: var(--text); }
  .axis-label { font-family: "Century Gothic", "Didact Gothic", sans-serif; font-size: 12px; fill: var(--text); }
  .axis-title { font-family: "Century Gothic", "Poppins", sans-serif; font-weight: 600; font-size: 12px; fill: var(--text); }
  .legend-label { font-family: "Century Gothic", "Didact Gothic", sans-serif; font-size: 12px; fill: var(--text); }
</style>
</head>
<body>
<main class="page">

  <section class="lending-matrix" aria-label="Lending process matrix">
    <svg class="matrix-arrows" viewBox="0 0 944 620" aria-hidden="true">
      <rect x="455" y="104" width="11" height="452" fill="var(--gold-soft)"/>
      <polygon points="460,86 441,108 480,108" fill="var(--gold-soft)"/>
      <polygon points="460,575 441,553 480,553" fill="var(--gold-soft)"/>
      <rect x="236" y="325" width="448" height="11" fill="var(--gold-soft)"/>
      <polygon points="216,330 240,311 240,349" fill="var(--gold-soft)"/>
      <polygon points="702,330 678,311 678,349" fill="var(--gold-soft)"/>
    </svg>
    <div class="matrix-tile tile-origination">Origination &amp; assessment</div>
    <div class="matrix-tile tile-documentation">Loan documentation &amp; settlement</div>
    <div class="matrix-tile tile-asset">Asset management</div>
    <div class="matrix-tile tile-portfolio">Portfolio management</div>
  </section>

  <figure class="chart-frame">
    <svg width="636" height="370" viewBox="0 0 636 370" role="img" aria-label="Line chart of unemployment rate by year, 1996 to 2016">
      <text class="chart-title" x="319" y="36" text-anchor="middle">Unemployment Rate</text>

      <g class="chart-grid" stroke="var(--grid)" stroke-width="1">
        <line x1="76" y1="62" x2="522" y2="62"/>
        <line x1="76" y1="86.1" x2="522" y2="86.1"/>
        <line x1="76" y1="110.2" x2="522" y2="110.2"/>
        <line x1="76" y1="134.3" x2="522" y2="134.3"/>
        <line x1="76" y1="158.4" x2="522" y2="158.4"/>
        <line x1="76" y1="182.5" x2="522" y2="182.5"/>
        <line x1="76" y1="206.6" x2="522" y2="206.6"/>
        <line x1="76" y1="230.7" x2="522" y2="230.7"/>
        <line x1="76" y1="254.8" x2="522" y2="254.8"/>
        <line x1="76" y1="278.9" x2="522" y2="278.9"/>
        <line x1="76" y1="303" x2="522" y2="303"/>
        <line x1="76" y1="62" x2="76" y2="303"/>
      </g>

      <g class="axis-label" text-anchor="end">
        <text x="66" y="66">10%</text>
        <text x="66" y="90">9%</text>
        <text x="66" y="114">8%</text>
        <text x="66" y="138">7%</text>
        <text x="66" y="162">6%</text>
        <text x="66" y="186">5%</text>
        <text x="66" y="210">4%</text>
        <text x="66" y="235">3%</text>
        <text x="66" y="259">2%</text>
        <text x="66" y="283">1%</text>
        <text x="66" y="307">0%</text>
      </g>

      <g class="axis-label" text-anchor="middle">
        <text x="118" y="327">1996</text>
        <text x="191" y="327">2000</text>
        <text x="265" y="327">2004</text>
        <text x="338" y="327">2008</text>
        <text x="412" y="327">2012</text>
        <text x="485" y="327">2016</text>
      </g>

      <text class="axis-title" x="299" y="350" text-anchor="middle">Year</text>
      <text class="axis-title" x="0" y="0" text-anchor="middle" transform="translate(31 182) rotate(-90)">Percent</text>

      <polyline class="series-line" points="118,86.1 191,158.4 265,182.5 338,206.6 412,182.5 485,158.4" fill="none" stroke="var(--logo-blue)" stroke-width="4" stroke-linejoin="round"/>
      <g class="series-markers" fill="var(--gold)" stroke="var(--logo-blue)" stroke-width="1.5">
        <polygon points="118,80 124,86.1 118,92 112,86.1"/>
        <polygon points="191,152 197,158.4 191,164 185,158.4"/>
        <polygon points="265,176 271,182.5 265,188 259,182.5"/>
        <polygon points="338,200 344,206.6 338,212 332,206.6"/>
        <polygon points="412,176 418,182.5 412,188 406,182.5"/>
        <polygon points="485,152 491,158.4 485,164 479,158.4"/>
      </g>

      <g class="chart-legend">
        <line x1="536" y1="208" x2="558" y2="208" stroke="var(--logo-blue)" stroke-width="3"/>
        <polygon points="547,203 552,208 547,213 542,208" fill="var(--gold)" stroke="var(--logo-blue)" stroke-width="1"/>
        <text class="legend-label" x="562" y="204">Unemploy-</text>
        <text class="legend-label" x="562" y="219">ment rate</text>
      </g>
    </svg>
  </figure>

</main>
</body>
</html>
```